Managed IT services business card design

We haven't needed a business card since the founding of the business in 2005. All our clients have been coming through word of mouth. And lately more and more existing clients are requesting for our business cards to pass on to their contacts in recommending us.
So we needing a business card design. We use various innovative solutions and methodologies to provide IT services to small businesses in managing their IT systems. Our role is the same as an in-house, full-time IT Manager for our clients, but outsourced. So we take care of all our clients' IT needs, just as an IT Manager would be expected to perform.
We have a holding website, which we're happy to leave for now. If we can use the same logo would be great - www.tegvu.com.au
Preferred colours are shades of are white, grey and black.
We pride our business with the following traits: proactive, good service, prompt response, trustworthy.
Target Market(s)
Small businesses of any industry
Industry/Entity Type
Business

```html
<!DOCTYPE html>
<html lang="en">
<head>
<meta charset="utf-8">
<title>tegvu business card</title>
<link rel="stylesheet" href="https://fonts.googleapis.com/css2?family=Courier+Prime:wght@400;700&display=swap">
<style>
  :root {
    --backdrop: #e4e4e2;
    --card: #ffffff;
    --ink: #111111;
    --ink-soft: #3a3a3a;
    --rule: #8a8a8a;
  }
  * { margin: 0; padding: 0; box-sizing: border-box; }
  html, body {
    width: 1200px;
    height: 1180px;
    overflow: hidden;
    background: var(--backdrop);
  }
  .stage {
    width: 1200px;
    height: 1180px;
    display: flex;
    align-items: center;
    justify-content: center;
  }
  .business-card {
    position: relative;
    width: 900px;
    height: 550px;
    background: var(--card);
    box-shadow: 0 10px 30px rgba(0,0,0,0.12);
    font-family: "Courier Prime", "Courier New", monospace;
    color: var(--ink);
  }
  .brand {
    position: absolute;
    left: 80px;
    top: 130px;
    display: flex;
    align-items: center;
    gap: 28px;
  }
  .brand-name {
    font-size: 76px;
    font-weight: 700;
    letter-spacing: 6px;
    line-height: 1;
  }
  .brand-square {
    width: 22px;
    height: 22px;
    background: var(--ink);
  }
  .tagline {
    position: absolute;
    left: 82px;
    top: 230px;
    font-size: 21px;
    color: var(--ink-soft);
  }
  .contact-row {
    position: absolute;
    left: 82px;
    right: 120px;
    top: 360px;
    display: flex;
    gap: 26px;
    font-size: 21px;
    color: var(--ink-soft);
  }
  .contact-item {
    display: flex;
    align-items: center;
    gap: 8px;
    white-space: nowrap;
  }
  .contact-icon { width: 18px; height: 18px; flex: none; }
  .divider {
    position: absolute;
    left: 82px;
    right: 130px;
    top: 400px;
    border-top: 2px solid var(--rule);
  }
  .address {
    position: absolute;
    left: 82px;
    top: 424px;
    font-size: 21px;
    color: var(--ink-soft);
  }
</style>
</head>
<body>
<main class="stage">
  <article class="business-card">
    <div class="brand">
      <span class="brand-name">tegvu</span>
      <span class="brand-square"></span>
    </div>
    <p class="tagline">managed i.t. services and consulting</p>

    <div class="contact-row">
      <span class="contact-item">
        <svg class="contact-icon" viewBox="0 0 24 24" aria-hidden="true">
          <path fill="currentColor" d="M6.6 10.8a15.1 15.1 0 0 0 6.6 6.6l2.2-2.2a1 1 0 0 1 1-.25 11.4 11.4 0 0 0 3.6.57 1 1 0 0 1 1 1V20a1 1 0 0 1-1 1A17 17 0 0 1 3 4a1 1 0 0 1 1-1h3.5a1 1 0 0 1 1 1c0 1.25.2 2.45.57 3.57a1 1 0 0 1-.25 1z"/>
        </svg>
        +61 400 555 018
      </span>
      <span class="contact-item">
        <svg class="contact-icon" viewBox="0 0 24 24" aria-hidden="true">
          <rect x="2.5" y="5" width="19" height="14" fill="none" stroke="currentColor" stroke-width="2"/>
          <path d="M3 6l9 7 9-7" fill="none" stroke="currentColor" stroke-width="2"/>
        </svg>
        mail@tegvu.com.au
      </span>
      <span class="contact-item">
        <svg class="contact-icon" viewBox="0 0 24 24" aria-hidden="true">
          <circle cx="12" cy="12" r="9.5" fill="none" stroke="currentColor" stroke-width="2"/>
          <ellipse cx="12" cy="12" rx="4" ry="9.5" fill="none" stroke="currentColor" stroke-width="1.6"/>
          <path d="M2.5 12h19" stroke="currentColor" stroke-width="1.6"/>
        </svg>
        www.tegvu.com.au
      </span>
    </div>

    <div class="divider"></div>
    <p class="address">harlow lane, melbourne</p>
  </article>
</main>
</body>
</html>
```